High end boutique food product label

We are looking for a label design to be used on our range of high end food products. We don't have a design or colour scheme in mind and are interested to see what ideas are submitted.
We would like it to feel sophisticated, chic, and eye-catching.
All of our products are handmade in Australia using Australian ingredients.
The graphics for the label will need to be scaleable to be fit a variety of labels from small squat jars with labels sized 3.5cm high and 7cm wide, to tall thin bottles with labels that are 14cm high and 4.5cm wide.
We would be interested in working with the winning designer to create these different sized labels.
The label submitted for this project should be 14cm high and 4.5cm wide, it should include our logo (file supplied in .jpeg and .ai), the product name 'Extra Virgin Olive Oil' and the size '250ml'.
This is just the front label on a bottle, we are not expecting a rear label to be created currently.
You are welcome to use any fonts you think will look good but the fonts used in our logo are Allaina Medium and Bebas Kai Regular.

```html
<!DOCTYPE html>
<html lang="en">
<head>
<meta charset="utf-8">
<title>Extra Virgin Olive Oil – Front Label</title>
<link rel="stylesheet" href="https://fonts.googleapis.com/css2?family=Playfair+Display:wght@400&family=Cormorant+Garamond:wght@500&display=swap">
<style>
  :root {
    --olive-green: #9c9a1f;
    --earth-brown: #7b3a12;
    --deep-plum: #2a0b46;
    --wine: #4a0a3a;
    --cream: #f4eed6;
    --brand-gold: #a8a423;
  }
  html, body {
    margin: 0;
    padding: 0;
    width: 1200px;
    height: 3736px;
    overflow: hidden;
    background: var(--olive-green);
  }
  .label {
    position: relative;
    width: 1200px;
    height: 3736px;
    overflow: hidden;
    background: var(--olive-green);
  }
  .olive-artwork {
    position: absolute;
    left: 0;
    top: 0;
    width: 1200px;
    height: 2540px;
    display: block;
  }
  .brand {
    position: absolute;
    top: 190px;
    left: 0;
    width: 100%;
    display: flex;
    justify-content: center;
    align-items: center;
    gap: 22px;
  }
  .brand-dot {
    width: 34px;
    height: 34px;
    border-radius: 50%;
    background: var(--brand-gold);
  }
  .brand-name {
    font-family: "Cormorant Garamond", serif;
    font-weight: 500;
    font-size: 84px;
    line-height: 1;
    color: var(--brand-gold);
  }
  .product-info {
    position: absolute;
    top: 2540px;
    left: 0;
    width: 100%;
    height: 1196px;
    text-align: center;
    color: var(--cream);
    font-family: "Playfair Display", serif;
    font-weight: 400;
  }
  .product-variety {
    position: absolute;
    top: 320px;
    width: 100%;
    margin: 0;
    font-size: 72px;
    line-height: 1;
  }
  .product-name {
    position: absolute;
    top: 460px;
    width: 100%;
    margin: 0;
    font-size: 124px;
    letter-spacing: 14px;
    line-height: 1;
    font-weight: 400;
  }
  .product-origin {
    position: absolute;
    top: 700px;
    width: 100%;
    margin: 0;
    font-size: 52px;
    line-height: 1;
  }
  .product-volume {
    position: absolute;
    top: 1010px;
    width: 100%;
    margin: 0;
    font-size: 58px;
    line-height: 1;
  }
</style>
</head>
<body>
  <main class="label">
    <svg class="olive-artwork" viewBox="0 0 1200 2540" role="img" aria-label="Stylised illustration of dark purple olives on green branches over an earthy brown background">
      <defs>
        <linearGradient id="olive-tones" x1="0" y1="0" x2="1" y2="1">
          <stop offset="0" stop-color="var(--deep-plum)"/>
          <stop offset="0.45" stop-color="var(--wine)"/>
          <stop offset="0.75" stop-color="var(--deep-plum)"/>
          <stop offset="1" stop-color="var(--earth-brown)"/>
        </linearGradient>
      </defs>
      <rect width="1200" height="2540" fill="url(#olive-tones)"/>
    </svg>

    <header class="brand">
      <span class="brand-dot"></span>
      <span class="brand-name">Hollis &amp; Reed</span>
    </header>

    <section class="product-info">
      <p class="product-variety">Extra Virgin</p>
      <h1 class="product-name">OLIVE OIL</h1>
      <p class="product-origin">100% Australian made</p>
      <p class="product-volume">250ml</p>
    </section>
  </main>
</body>
</html>
```